【 概要 】 起業塾メディアサイトのメインバナーのデザイン作成をお願いします。 【 依頼内容 】 ・サイズ: 横2300 × 縦1200px ・作成数: 1種類 【 デザインイメージ 】 ・ターゲット層:起業塾の利用検討者向け ・雰囲気:リアルな実体験が載っていそうな雰囲気 【 使用素材 】 (使用テキスト) 最新2023年の起業塾の徹底比較、評判まとめサイトの決定版 現役起業家が100人以上へのアンケート実施や潜入体験レポート。1サービス平均10時間以上の徹底調査 (使用画像) フリー素材を使いつつも、フリー素材に見えにくい形だと助かります。 |
文字の視認性が高く、イラスト風なデザインも好みだったので採用させていただきました!
皆さん、ご提案ありがとうございました!またの機会がありましたら応募させていただきますので、よろしくお願いします!

```html
<!DOCTYPE html>
<html lang="ja">
<head>
<meta charset="UTF-8">
<title>起業塾 徹底比較バナー</title>
<link rel="stylesheet" href="https://fonts.googleapis.com/css2?family=Noto+Sans+JP:wght@700;900&display=swap">
<style>
  :root {
    --navy: #14266a;
    --navy-deep: #0e1c52;
    --blue: #1a4fb8;
    --yellow: #f7e62b;
    --ink: #0b0b14;
    --pink: #f06ad6;
    --sky: #8fb0ff;
    --white: #ffffff;
  }
  * { margin: 0; padding: 0; box-sizing: border-box; }
  html, body { width: 1200px; height: 626px; overflow: hidden; background: var(--white); }
  body { font-family: "Noto Sans JP", sans-serif; }

  .banner { position: relative; width: 1200px; height: 626px; overflow: hidden; }

  .scene-photo {
    position: absolute; inset: 0;
    background:
      radial-gradient(ellipse at 78% 40%, rgba(255,255,255,0.85), rgba(255,255,255,0) 60%),
      linear-gradient(120deg, #d9dee6 0%, #eef1f5 35%, #e4e9f1 60%, #c9d6ea 100%);
  }

  .top-band {
    position: absolute; left: 0; top: 0; width: 1200px; height: 64px;
    background: var(--navy);
  }
  .top-title {
    position: absolute; left: 14px; top: 0; height: 64px;
    display: flex; align-items: center;
    color: var(--white); font-weight: 900; font-size: 50px; letter-spacing: 2px;
    font-style: italic;
  }
  .top-badge {
    position: absolute; left: 580px; top: 4px; width: 162px; height: 58px;
    background: var(--yellow); color: var(--navy-deep);
    display: flex; align-items: center; justify-content: center;
    font-weight: 900; font-size: 46px; letter-spacing: 2px;
  }

  .headline-panel {
    position: absolute; left: 180px; top: 145px; width: 900px; height: 300px;
    background: linear-gradient(90deg, rgba(255,255,255,0) 0%, rgba(255,255,255,0.92) 12%, rgba(255,255,255,0.92) 88%, rgba(255,255,255,0) 100%);
  }

  .year-line {
    position: absolute; left: 0; width: 1200px; top: 170px; text-align: center;
    color: var(--blue); font-weight: 900; font-size: 46px; letter-spacing: 1px;
  }
  .year-line .particle { font-size: 36px; color: var(--navy-deep); }
  .rule {
    position: absolute; left: 290px; top: 238px; width: 720px; height: 3px;
    background: var(--navy-deep);
  }

  .latest {
    position: absolute; left: 196px; top: 186px; width: 86px;
    display: flex; flex-direction: column; align-items: center;
    color: var(--blue); font-weight: 900; font-size: 78px; line-height: 1;
    -webkit-text-stroke: 3px var(--white); paint-order: stroke fill;
    text-shadow: 0 0 6px rgba(255,255,255,0.9);
  }

  .compare {
    position: absolute; left: 290px; top: 236px;
    font-weight: 900; font-size: 184px; line-height: 1; letter-spacing: 4px;
    color: var(--ink);
    text-shadow: 8px 8px 0 var(--pink), -6px -4px 0 var(--sky);
  }

  .sub-band {
    position: absolute; left: 0;
    background: var(--navy);
    color: var(--white); font-weight: 900; font-style: italic;
    display: flex; align-items: center; padding-left: 16px;
    clip-path: polygon(0 0, 100% 0, calc(100% - 14px) 100%, 0 100%);
  }
  .sub-band.survey { top: 476px; width: 1186px; height: 58px; font-size: 31px; }
  .sub-band.survey .num { font-size: 38px; }
  .sub-band.research { top: 556px; width: 880px; height: 56px; font-size: 31px; }
  .sub-band.research .num { font-size: 40px; }
</style>
</head>
<body>
<div class="banner">
  <div class="scene-photo" role="img" aria-label="オフィスで資料を手に打ち合わせをするビジネスパーソンとグラフ資料の写真"></div>

  <div class="top-band"></div>
  <div class="top-title">評判まとめサイトの</div>
  <div class="top-badge">決定版</div>

  <div class="headline-panel"></div>
  <div class="year-line">2023年<span class="particle">の</span>起業塾</div>
  <div class="rule"></div>
  <div class="latest"><span>最</span><span>新</span></div>
  <div class="compare">徹底比較</div>

  <div class="sub-band survey">現役起業家が<span class="num">100</span>人以上へのアンケート実施や潜入体験レポート</div>
  <div class="sub-band research"><span class="num">1</span>サービス平均<span class="num">10</span>時間以上の徹底調査</div>
</div>
</body>
</html>
```